engaging mobile application to encourage lifestyle change

We need an App that will help people get from Bold 4 Bloom. A weight loss program based on realistic and healthy lifestyle modifications. By learning portion control, healthy food choices, and with the encouragement to get moving.
We would like the design to be gender neutral but must be fun.
The final design must be easy to use and useful to our clients.

Target Market(s)

Health, Wellbeing, Weightloss

Industry/Entity Type

Weight

Font styles to use
Sans Serif

Requirements
Must have
• Hydration log, Weigh-ins with fat %, Food log, Location of meetings,lectures and weigh-ins, list of restaurants that comply with B4B, Fitness plan, Mall walk maps, daily motivational message.

```html
<!DOCTYPE html>
<html lang="en">
<head>
<meta charset="utf-8">
<title>Bold 4 Bloom – Log</title>
<link rel="stylesheet" href="https://fonts.googleapis.com/css2?family=Roboto:wght@300;400;500&display=swap">
<style>
  :root {
    --status-teal: #45c1d1;
    --status-teal-dark: #36b3c6;
    --brand-orange: #ff9a0a;
    --brand-orange-light: #ffab2e;
    --tab-idle: #ffd9a3;
    --tab-active: #ffffff;
    --tab-indicator: #5ab8d8;
    --ink: #222222;
    --ink-soft: #666666;
    --divider: #dcdcdc;
    --section-bg: #ffffff;
    --under-green: #18a06e;
    --accent-blue: #7cc6e6;
    --fab-blue: #7ec5e5;
    --info-grey: #6a6a6a;
    --page: #ffffff;
    --thumb-dairy: #ece6e6;
    --thumb-grain: #d8c49a;
    --thumb-sandwich: #dccb9c;
    --thumb-fruit: #d98a80;
    --thumb-veg: #c4dca0;
  }
  * { box-sizing: border-box; margin: 0; padding: 0; }
  html, body { width: 750px; height: 1200px; overflow: hidden; }
  body { background: var(--page); font-family: 'Roboto', Arial, sans-serif; color: var(--ink); }
  .screen { position: relative; width: 750px; height: 1200px; overflow: hidden; background: var(--section-bg); }

  .status-bar { position: absolute; top: 0; left: 0; width: 750px; height: 52px;
    background: linear-gradient(90deg, var(--status-teal), var(--status-teal-dark)); }
  .status-bar .signal { position: absolute; left: 606px; top: 26px; }
  .status-bar .battery { position: absolute; left: 651px; top: 24px; width: 14px; height: 22px; background: #fff; border-radius: 2px; }
  .status-bar .time { position: absolute; left: 678px; top: 22px; font-size: 24px; font-weight: 500; color: #fff; }

  .app-bar { position: absolute; top: 52px; left: 0; width: 750px; height: 201px;
    background: linear-gradient(100deg, var(--brand-orange-light) 0%, var(--brand-orange-light) 45%, var(--brand-orange) 45%);
    box-shadow: 0 3px 6px rgba(0,0,0,.18); }
  .app-title { position: absolute; left: 52px; top: 40px; font-size: 40px; font-weight: 400; color: #fff; letter-spacing: .5px; }
  .action { position: absolute; top: 36px; }
  .action.todo { left: 412px; }
  .action.trophy { left: 505px; }
  .action.chat { left: 596px; }
  .action.more { left: 706px; }
  .badge { position: absolute; left: 602px; top: 30px; width: 36px; height: 36px; border-radius: 50%;
    background: #e31b23; border: 3px solid #fff; color: #fff; font-size: 20px; font-weight: 500;
    display: flex; align-items: center; justify-content: center; }

  .tabs { position: absolute; left: 0; top: 145px; width: 750px; height: 56px; }
  .tab { position: absolute; top: 0; width: 188px; margin-left: -94px; text-align: center;
    font-size: 24px; color: var(--tab-idle); text-transform: uppercase; }
  .tab.active { color: var(--tab-active); }
  .tab-indicator { position: absolute; left: 188px; top: 50px; width: 188px; height: 5px; background: var(--tab-indicator); }

  .summary { position: absolute; top: 253px; left: 0; width: 750px; height: 107px; border-bottom: 2px solid var(--divider); }
  .summary-item { position: absolute; top: 18px; width: 150px; margin-left: -75px; text-align: center; }
  .summary-label { font-size: 20px; color: var(--ink-soft); }
  .summary-value { font-size: 40px; color: var(--ink); margin-top: 2px; }
  .summary-value.under { display: inline-block; background: var(--under-green); color: #fff; padding: 2px 8px; }

  .meal-header { position: absolute; left: 22px; width: 700px; font-size: 28px; color: var(--ink-soft); }
  .info-icon { position: absolute; right: 0; top: 0; }

  .entry { position: absolute; left: 0; width: 750px; height: 100px; }
  .entry-thumb { position: absolute; left: 30px; top: 2px; width: 74px; height: 74px; border-radius: 8px; }
  .entry-name { position: absolute; left: 121px; top: 0; font-size: 32px; color: var(--ink); white-space: nowrap; }
  .entry-portion { position: absolute; left: 121px; top: 44px; font-size: 23px; color: var(--ink-soft); }
  .entry-cals { position: absolute; right: 37px; top: 18px; font-size: 32px; color: var(--ink); }

  .thumb-milk { background: var(--thumb-dairy); }
  .thumb-oats { background: var(--thumb-grain); }
  .thumb-sandwich { background: var(--thumb-sandwich); }
  .thumb-apple { background: var(--thumb-fruit); }
  .thumb-celery { background: var(--thumb-veg); }

  .section-divider { position: absolute; left: 104px; top: 662px; width: 646px; height: 2px; background: var(--divider); }

  .day-nav { position: absolute; top: 1095px; left: 0; width: 750px; height: 70px; }
  .day-label { position: absolute; left: 0; width: 750px; text-align: center; top: 4px; font-size: 44px; font-weight: 300; color: var(--accent-blue); }
  .day-prev { position: absolute; left: 180px; top: 12px; }
  .day-next { position: absolute; left: 548px; top: 12px; }

  .fab { position: absolute; left: 582px; top: 1056px; width: 122px; height: 122px; border-radius: 50%;
    background: var(--fab-blue); box-shadow: 0 4px 8px rgba(0,0,0,.25); display: flex; align-items: center; justify-content: center; }
</style>
</head>
<body>
<main class="screen">
  <div class="status-bar">
    <svg class="signal" width="24" height="20" viewBox="0 0 24 20"><polygon points="24,0 24,20 0,20" fill="#fff"/></svg>
    <div class="battery"></div>
    <span class="time">4:37</span>
  </div>

  <header class="app-bar">
    <h1 class="app-title">BOLD 4 BLOOM</h1>
    <svg class="action todo" width="50" height="46" viewBox="0 0 50 46" aria-label="Checklist">
      <g fill="none" stroke="#fff" stroke-width="5" stroke-linecap="round">
        <line x1="4" y1="6" x2="40" y2="6"/><line x1="4" y1="18" x2="30" y2="18"/><line x1="4" y1="30" x2="18" y2="30"/>
        <polyline points="18,30 26,40 46,10"/>
      </g>
    </svg>
    <svg class="action trophy" width="52" height="48" viewBox="0 0 52 48" aria-label="Achievements">
      <g fill="#fff">
        <path d="M12 2h28v14c0 9-6 15-14 15S12 25 12 16z"/>
        <path d="M12 6H3v5c0 7 5 11 11 11v-4c-4 0-7-3-7-7V10h5z"/>
        <path d="M40 6h9v5c0 7-5 11-11 11v-4c4 0 7-3 7-7V10h-5z"/>
        <rect x="23" y="30" width="6" height="8"/>
        <rect x="15" y="38" width="22" height="7" rx="1"/>
      </g>
    </svg>
    <svg class="action chat" width="50" height="50" viewBox="0 0 50 50" aria-label="Messages">
      <path d="M6 8h38a4 4 0 0 1 4 4v20a4 4 0 0 1-4 4H30l-4 10-4-10H6a4 4 0 0 1-4-4V12a4 4 0 0 1 4-4z" fill="#fff"/>
    </svg>
    <div class="badge">1</div>
    <svg class="action more" width="12" height="48" viewBox="0 0 12 48" aria-label="More">
      <g fill="#fff"><circle cx="6" cy="6" r="5"/><circle cx="6" cy="24" r="5"/><circle cx="6" cy="42" r="5"/></g>
    </svg>

    <nav class="tabs">
      <span class="tab" style="left:93px">My Day</span>
      <span class="tab active" style="left:280px">Log</span>
      <span class="tab" style="left:470px">Goals</span>
      <span class="tab" style="left:657px">News Feed</span>
      <div class="tab-indicator"></div>
    </nav>
  </header>

  <section class="summary">
    <div class="summary-item" style="left:83px"><div class="summary-label">Budget</div><div class="summary-value">1,861</div></div>
    <div class="summary-item" style="left:228px"><div class="summary-label">Food</div><div class="summary-value">670</div></div>
    <div class="summary-item" style="left:375px"><div class="summary-label">Exercise</div><div class="summary-value">0</div></div>
    <div class="summary-item" style="left:522px"><div class="summary-label">Net</div><div class="summary-value">670</div></div>
    <div class="summary-item" style="left:668px"><div class="summary-label">Under</div><div class="summary-value under">1,191</div></div>
  </section>

  <div class="meal-header" style="top:383px">Breakfast: 192
    <svg class="info-icon" width="30" height="30" viewBox="0 0 30 30"><circle cx="15" cy="15" r="14" fill="var(--info-grey)"/><rect x="13" y="12" width="4" height="11" fill="#fff"/><circle cx="15" cy="8" r="2.3" fill="#fff"/></svg>
  </div>

  <div class="entry" style="top:462px">
    <div class="entry-thumb thumb-milk" role="img" aria-label="Illustration of a milk carton"></div>
    <div class="entry-name">Milk, Skim, w/ Vitamin A &amp; D</div>
    <div class="entry-portion">1/2 Cup</div>
    <div class="entry-cals">42</div>
  </div>

  <div class="entry" style="top:576px">
    <div class="entry-thumb thumb-oats" role="img" aria-label="Illustration of an oat stalk"></div>
    <div class="entry-name">Oats, Rolled, Old Fashioned</div>
    <div class="entry-portion">1/2 Cup</div>
    <div class="entry-cals">150</div>
  </div>

  <div class="section-divider"></div>

  <div class="meal-header" style="top:688px">Lunch: 478
    <svg class="info-icon" width="30" height="30" viewBox="0 0 30 30"><circle cx="15" cy="15" r="14" fill="var(--info-grey)"/><rect x="13" y="12" width="4" height="11" fill="#fff"/><circle cx="15" cy="8" r="2.3" fill="#fff"/></svg>
  </div>

  <div class="entry" style="top:764px">
    <div class="entry-thumb thumb-sandwich" role="img" aria-label="Illustration of a sandwich"></div>
    <div class="entry-name">Sandwich, Ham Cheese, w/ Whol..</div>
    <div class="entry-portion">1 Each</div>
    <div class="entry-cals">363</div>
  </div>

  <div class="entry" style="top:877px">
    <div class="entry-thumb thumb-apple" role="img" aria-label="Illustration of an apple"></div>
    <div class="entry-name">Apple, Medium</div>
    <div class="entry-portion">1 Each</div>
    <div class="entry-cals">95</div>
  </div>

  <div class="entry" style="top:991px">
    <div class="entry-thumb thumb-celery" role="img" aria-label="Illustration of celery stalks"></div>
    <div class="entry-name">Celery, Stalk, Fresh, Med</div>
    <div class="entry-portion">3 Pieces</div>
    <div class="entry-cals">20</div>
  </div>

  <nav class="day-nav">
    <svg class="day-prev" width="24" height="46" viewBox="0 0 24 46"><polyline points="20,2 4,23 20,44" fill="none" stroke="var(--accent-blue)" stroke-width="3"/></svg>
    <div class="day-label">Wednesday</div>
    <svg class="day-next" width="24" height="46" viewBox="0 0 24 46"><polyline points="4,2 20,23 4,44" fill="none" stroke="var(--accent-blue)" stroke-width="3"/></svg>
  </nav>

  <div class="fab" aria-label="Add entry">
    <svg width="60" height="60" viewBox="0 0 64 64"><g stroke="#fff" stroke-width="6"><line x1="32" y1="4" x2="32" y2="60"/><line x1="4" y1="32" x2="60" y2="32"/></g></svg>
  </div>
</main>
</body>
</html>
```